Electrical Business Card Design

New electrical business targeting my local area
Installations
Repairs
Switchboards
TV / Vistacast / Antennas
Telephone
Data Networks
Audio Visual
Licence # 518427K
ABN 58316927405
I would like some white background, black writing, red, blue & green can be used
Designer discretion to be used on layout, colour placement & any images
Reason: To give designers more time, I thought 5 days wasn't enough
Please don't just create generic business cards................include personal details e.g. business name, contact name, ph #, email. Also include the things I do, licence # & abn (refer to brief for all details)
Thanks
Reason: Would like more designs & have now committed my payment, thank you
Industry/Entity Type
Electrical
Contact Information for Business Card
Korvane Electrical Services,
Gareth Pelling,
0438 571 963,
korvaneelectrical@wexmail.net.au,
My suburb is Ryde
Look and feel

```html
<!DOCTYPE html>
<html lang="en">
<head>
<meta charset="utf-8">
<title>Korvane Electrical Services</title>
<link rel="stylesheet" href="https://fonts.googleapis.com/css2?family=Arimo:wght@700&display=swap">
<style>
  :root {
    --brand-blue: #0b4edc;
    --ink: #050505;
    --accent-green: #5cff00;
  }
  html, body {
    margin: 0;
    padding: 0;
    overflow: hidden;
  }
  .card {
    position: relative;
    width: 686px;
    height: 1200px;
    background: var(--brand-blue);
    overflow: hidden;
    font-family: "Arimo", Arial, sans-serif;
  }
  .business-name {
    position: absolute;
    left: 0;
    width: 698px;
    top: 473px;
    margin: 0;
    text-align: center;
    color: var(--ink);
    font-size: 66px;
    line-height: 80px;
    font-weight: 700;
  }
  .business-name span { display: block; }
  .value-connector {
    position: absolute;
    left: 0;
    top: 0;
  }
  .value-tag {
    position: absolute;
    left: 500px;
    width: 157px;
    height: 42px;
    border-radius: 21px;
    background: var(--accent-green);
    color: var(--ink);
    font-size: 27px;
    font-weight: 700;
    line-height: 42px;
    text-align: center;
  }
  .value-tag--reliable { top: 1064px; }
  .value-tag--honest { top: 1119px; }
</style>
</head>
<body>
  <main class="card">
    <h1 class="business-name">
      <span>Korvane</span>
      <span>Electrical</span>
      <span>Services</span>
    </h1>

    <svg class="value-connector" width="686" height="1200" viewBox="0 0 686 1200" aria-hidden="true">
      <g fill="none" stroke="#5cff00" stroke-width="3">
        <line x1="0" y1="1111" x2="461" y2="1111"/>
        <polyline points="500,1085 461,1085 461,1140 500,1140"/>
      </g>
    </svg>

    <div class="value-tag value-tag--reliable">Reliable</div>
    <div class="value-tag value-tag--honest">Honest</div>
  </main>
</body>
</html>
```